Minimalistic logo and website for plovrek.com

My colleague and I just started a new company. We need a website to replace the Stenhus at https://plovrek.com/

We need a onepager website. A logotype and color profiles. We like minimalism. Scandinavian design.

Below is just information about the company. You can rearrange it, add photos, emit stuff. Maybe even add stuff if you think it is necessary.

# About Plovrek
Plovrek builds critical applications to capture new markets, create modern services and captivate our customers in new and engaging ways. Creating effective and engaging solutions that truly work has always been Plovrek's core offering and is what makes us excited to work in digital. We are a forward thinking company embracing the opportunities of digital transformation and automations.

# Core services
Business automation
Application development and services for desktop and mobile
Interface Design and UX
Enterprise integrations

# Some more data
Plovrek was founded by Torvald Ekblom and Mikael Grundberg in 2021.
Vendalink: https://www.vendalink.com/company/58402917/admin/

# Inspiration
Minimal. Simple.
https://www.kvarnbyformverk.se/contact

Target Market(s)

Businesses

Industry/Entity Type

IT, business automation, data

Number of Pages Required

1 page

Font styles to use
Sans Serif

Colors

Designer to choose colors to be used in the design.

Requirements
Must have
• Onepage design. Minimalism.
Should not have
• Menus

```html
<!DOCTYPE html>
<html lang="en">
<head>
<meta charset="utf-8">
<title>Plovrek</title>
<link rel="stylesheet" href="https://fonts.googleapis.com/css2?family=Oswald:wght@500;600&family=Poppins:wght@400;500;600&display=swap">
<style>
:root{
  --yellow:#ffcc00;
  --yellow-dark:#e0b000;
  --black:#0b0b0b;
  --ink:#111111;
  --grey-bg:#f2f2f2;
  --muted:#7a7a7a;
  --beige:#f2e9df;
  --white:#ffffff;
}
*{margin:0;padding:0;box-sizing:border-box}
html,body{width:1200px;height:3861px;overflow:hidden}
body{position:relative;background:var(--white);font-family:'Poppins',sans-serif;color:var(--ink)}
.abs{position:absolute}
.heading{font-family:'Oswald',sans-serif;font-weight:600;letter-spacing:.2px}
.bg-shape{position:absolute;left:0;top:0}
.brand{font-family:'Poppins',sans-serif;font-weight:600;color:var(--yellow);font-size:46px;letter-spacing:.5px}

/* hero */
.hero-title{left:63px;top:200px;color:var(--white);font-size:58px;line-height:68px}
.hero-art{left:420px;top:100px;width:400px;height:490px;background:radial-gradient(ellipse at 55% 40%,rgba(110,70,35,.75) 0%,rgba(40,42,52,.6) 38%,rgba(11,11,11,0) 70%)}
.dot{border-radius:50%;background:var(--yellow)}
.hero-text{left:740px;top:236px;width:398px;text-align:right;color:var(--white);font-size:15px;line-height:23px}
.plus-btn{display:flex;align-items:center;gap:18px;font-size:13px;font-weight:500;color:var(--white)}
.plus{width:38px;height:38px;border-radius:50%;background:#2c2c2c;display:flex;align-items:center;justify-content:center}
.hero-card{left:771px;top:389px;width:382px;height:248px;background:var(--white);border-radius:10px;box-shadow:0 12px 30px rgba(0,0,0,.12)}
.hero-card .inner{position:absolute;left:17px;top:15px;width:350px;height:228px;background:var(--beige)}
.hero-card .ball{position:absolute;left:22px;top:38px;width:100px;height:100px;border-radius:50%;background:#1d1d1d}
.hero-card p{position:absolute;left:151px;top:72px;width:180px;font-size:17px;font-weight:600;line-height:26px}
.slide-no{left:60px;top:590px;color:var(--white);font-size:11px;display:flex;gap:6px}
.slide-no span{display:block;width:34px}
.slide-no span i{display:block;height:2px;background:var(--white);margin-bottom:5px}

/* partners */
.partners{top:732px;left:0;width:1200px;height:40px}
.partner{position:absolute;top:0;display:flex;align-items:center;gap:10px;font-size:24px;font-weight:500;color:#3a3a3a;transform:translateX(-50%);white-space:nowrap}
.partner b{display:block;width:22px;height:22px;border-radius:50%;background:#3a3a3a}

/* about */
.photo{position:absolute}
.about h2{position:absolute;left:676px;top:884px;font-size:36px}
.about h3{position:absolute;left:676px;top:950px;width:400px;font-size:17px;font-weight:600;line-height:26px}
.about p{position:absolute;left:676px;top:1010px;width:380px;font-size:11.5px;line-height:19.5px;color:var(--muted)}
.call{left:676px;top:1155px;width:261px;height:60px;background:var(--yellow);display:flex}
.call .ic{width:73px;background:var(--yellow-dark);display:flex;align-items:center;justify-content:center}
.call .txt{padding:10px 0 0 40px;font-size:13px;font-weight:500;line-height:22px}
.call .txt strong{font-size:16px;font-weight:600}

/* services */
.services-title{left:0;width:1200px;top:1517px;text-align:center;font-size:36px}
.svc-photo{width:172px;height:172px;border-radius:50%;border:4px solid var(--yellow);margin:-86px 0 0 -86px}
.num{font-family:'Oswald',sans-serif;font-weight:600;font-size:66px;color:var(--yellow);line-height:1}
.svc-label{font-size:14px;font-weight:600;line-height:22px}
.svc-desc{width:300px;font-size:12px;line-height:19.6px;color:#444}

/* work together */
.work h2{position:absolute;left:61px;top:2566px;font-size:36px}
.work h3{position:absolute;left:61px;top:2628px;font-size:17px;font-weight:600}
.work p{position:absolute;left:61px;top:2660px;width:310px;font-size:12px;line-height:19.5px}
.work .plus{background:#fff3b0}
.work .plus-btn{color:var(--ink)}
.work-art{left:540px;top:2536px;width:600px;height:336px;background:radial-gradient(ellipse at 45% 50%,rgba(255,255,255,.55) 0%,rgba(255,255,255,0) 65%)}

/* news */
.news-title{left:144px;top:2938px;font-size:36px}
.arrows{left:990px;top:2958px;display:flex;align-items:center;gap:10px}
.card{top:3007px;width:285px;height:390px;background:var(--white);box-shadow:0 6px 20px rgba(0,0,0,.08)}
.card .img{height:195px}
.card .meta{position:absolute;left:31px;top:222px;display:flex;gap:26px;font-size:11.5px;color:#333}
.card .meta span{display:flex;align-items:center;gap:8px}
.card h4{position:absolute;left:31px;top:252px;font-size:14px;font-weight:600}
.card p{position:absolute;left:31px;top:283px;width:235px;font-size:12px;line-height:19.5px;color:var(--muted)}
.card a{position:absolute;left:31px;top:350px;font-size:12px;font-weight:600;color:var(--ink);text-decoration:none}

/* footer */
.footer-col h5{font-size:18px;font-weight:600;color:var(--yellow);margin-bottom:14px}
.footer-col li{list-style:none;font-size:12px;color:#ddd;line-height:27px}
.contact-row{display:flex;gap:18px;font-size:12px;color:#ddd;line-height:19px;margin-bottom:18px;width:220px}
.social{display:flex;gap:10px;align-items:center}
.social span{display:flex;align-items:center;justify-content:center;width:30px;height:30px;border-radius:50%;background:var(--yellow);font-size:9px;font-weight:600;color:var(--ink)}
.bottom-bar{left:0;top:3812px;width:1200px;height:49px;background:var(--black);color:var(--white);font-size:12px;display:flex;justify-content:space-between;align-items:center;padding:12px 61px 0}
</style>
</head>
<body>

<svg class="bg-shape" width="1200" height="3861" viewBox="0 0 1200 3861">
  <polygon points="0,0 1200,0 1200,554 0,667" fill="#0b0b0b"/>
  <polygon points="0,1501 1200,1393 1200,2382 0,2509" fill="#f2f2f2"/>
  <polygon points="0,2509 1200,2382 1200,2872 0,2872" fill="#ffcc00"/>
  <defs><linearGradient id="ft" x1="0" y1="0" x2="1" y2="1"><stop offset="0" stop-color="#1e1e1e"/><stop offset="1" stop-color="#0e0e0e"/></linearGradient></defs>
  <polygon points="0,3535 1200,3460 1200,3861 0,3861" fill="url(#ft)"/>
</svg>

<!-- header -->
<div class="abs brand" style="left:58px;top:0">plovrek</div>

<!-- hero -->
<div class="abs hero-art" role="img" aria-label="Dark 3D cubes floating with warm orange light"></div>
<div class="abs dot" style="left:658px;top:156px;width:48px;height:48px"></div>
<div class="abs dot" style="left:418px;top:339px;width:50px;height:50px"></div>
<h1 class="abs heading hero-title">Creating effective<br>and Engaging<br>solutions</h1>
<p class="abs hero-text">Creating effective and engaging solutions that truly work has always been Plovrek's core offering and is what makes us excited to work in digital.</p>
<div class="abs plus-btn" style="left:59px;top:443px">
  <span class="plus"><svg width="16" height="16"><path d="M8 1v14M1 8h14" stroke="#ffcc00" stroke-width="2"/></svg></span>EXPLORE MORE
</div>
<div class="abs slide-no"><span><i></i><i style="width:24px"></i><i style="width:14px"></i></span>01</div>
<div class="abs hero-card">
  <div class="inner">
    <div class="ball" role="img" aria-label="Basketball balanced on a fingertip"></div>
    <p>Plovrek builds critical applications to capture new markets</p>
  </div>
</div>

<!-- partners -->
<div class="abs partners">
  <div class="partner" style="left:202px"><b></b>Corvane</div>
  <div class="partner" style="left:367px"><b></b>Lumo</div>
  <div class="partner" style="left:559px"><b></b>Fabrikk</div>
  <div class="partner" style="left:768px"><b></b>Brevlo</div>
  <div class="partner" style="left:980px"><b></b>Stenhus</div>
</div>

<!-- about -->
<section class="about">
  <div class="photo" style="left:115px;top:840px;width:337px;height:411px;background:linear-gradient(135deg,#c4c4c4,#8a8a8a)" role="img" aria-label="Black and white desk with laptops, keyboard and headphones"></div>
  <div class="photo" style="left:330px;top:1132px;width:262px;height:186px;background:linear-gradient(135deg,#b3bcc3,#6a6460)" role="img" aria-label="Team working together at computers"></div>
  <h2 class="heading">About Plovrek</h2>
  <h3>Plovrek builds critical applications to capture new markets</h3>
  <p>create modern services and captivate our customers in new and engaging ways. Creating effective and engaging solutions that truly work has always been Plovrek's core offering and is what makes us excited to work in digital. We are a forward thinking company embracing the opportunities of digital transformation and automations.</p>
  <div class="abs call">
    <div class="ic"><svg width="34" height="34" viewBox="0 0 24 24"><path d="M5 3h4l2 5-2.5 1.5a11 11 0 0 0 6 6L16 13l5 2v4a2 2 0 0 1-2 2A16 16 0 0 1 3 5a2 2 0 0 1 2-2z" fill="none" stroke="#111" stroke-width="1.6"/><path d="M14 3a7 7 0 0 1 7 7M14 6.5a3.5 3.5 0 0 1 3.5 3.5" fill="none" stroke="#111" stroke-width="1.6"/></svg></div>
    <div class="txt">CALL US<br><strong>+46 8 555 0142</strong></div>
  </div>
</section>

<!-- services -->
<h2 class="abs heading services-title">Our Services</h2>

<div class="abs svc-photo" style="left:600px;top:1675px;background:linear-gradient(135deg,#c9d3da,#7a848c)" role="img" aria-label="Person using a VR headset in an office"></div>
<div class="abs num" style="left:166px;top:1643px">01</div>
<div class="abs svc-label" style="left:246px;top:1673px">Business automation</div>
<p class="abs svc-desc" style="left:725px;top:1628px">create modern services and captivate our customers in new and engaging ways. Creating effective and engaging solutions that truly work has always been Plovrek's core offering and is what</p>

<div class="abs svc-photo" style="left:600px;top:1877px;background:linear-gradient(135deg,#d8d6d0,#8a8984)" role="img" aria-label="Hands on a laptop keyboard with a coffee cup"></div>
<p class="abs svc-desc" style="left:162px;top:1830px">create modern services and captivate our customers in new and engaging ways. Creating effective and engaging solutions that truly work has always been Plovrek's core offering and is what</p>
<div class="abs svc-label" style="left:690px;top:1848px;width:200px;text-align:right">Application development and services for desktop and mobile</div>
<div class="abs num" style="left:904px;top:1845px">02</div>

<div class="abs svc-photo" style="left:600px;top:2079px;background:linear-gradient(135deg,#e6dcd2,#948d86)" role="img" aria-label="Laptop on a desk seen from above"></div>
<div class="abs num" style="left:160px;top:2047px">03</div>
<div class="abs svc-label" style="left:246px;top:2077px">Interface Design and UX</div>
<p class="abs svc-desc" style="left:725px;top:2032px">create modern services and captivate our customers in new and engaging ways. Creating effective and engaging solutions that truly work has always been Plovrek's core offering and is what</p>

<div class="abs svc-photo" style="left:600px;top:2283px;background:linear-gradient(135deg,#c7c2bb,#78818a)" role="img" aria-label="Colleagues reviewing work on a computer"></div>
<p class="abs svc-desc" style="left:162px;top:2236px">create modern services and captivate our customers in new and engaging ways. Creating effective and engaging solutions that truly work has always been Plovrek's core offering and is what</p>
<div class="abs svc-label" style="left:720px;top:2277px">Enterprise integrations</div>
<div class="abs num" style="left:904px;top:2251px">04</div>

<!-- work together -->
<section class="work">
  <h2 class="heading">Let's Work Together</h2>
  <h3>Need Successful Project</h3>
  <p>Lorem Ipsum is simply dummy text of the printing and typesetting industry. Lorem Ipsum has been the industry's standard dummy text ever since the 1500s,</p>
  <div class="abs plus-btn" style="left:59px;top:2752px;font-size:12.5px">
    <span class="plus" style="width:36px;height:36px"><svg width="16" height="16"><path d="M8 1v14M1 8h14" stroke="#111" stroke-width="2"/></svg></span>ESTIMATE PROJECT
  </div>
  <div class="abs work-art" role="img" aria-label="Two people collaborating around a large document with message bubbles"></div>
</section>

<!-- news -->
<h2 class="abs heading news-title">Latest News</h2>
<div class="abs arrows">
  <svg width="22" height="14"><path d="M21 7H2M8 1L2 7l6 6" fill="none" stroke="#111" stroke-width="1.6"/></svg>
  <span style="width:1px;height:14px;background:#111"></span>
  <svg width="22" height="14"><path d="M1 7h19M14 1l6 6-6 6" fill="none" stroke="#ffcc00" stroke-width="1.6"/></svg>
</div>

<article class="abs card" style="left:142px">
  <div class="img" style="background:linear-gradient(135deg,#e8e8e8,#b0b0b0)" role="img" aria-label="Phone on a stand beside a keyboard"></div>
  <div class="meta"><span><svg width="12" height="13"><circle cx="6" cy="4" r="3" fill="none" stroke="#ffcc00" stroke-width="1.3"/><path d="M1 12a5 5 0 0 1 10 0" fill="none" stroke="#ffcc00" stroke-width="1.3"/></svg>By Admin</span><span><svg width="13" height="13"><rect x="1" y="2" width="11" height="10" fill="none" stroke="#ffcc00" stroke-width="1.2"/><path d="M1 5h11" stroke="#ffcc00"/></svg>Jan 18,2022</span></div>
  <h4>Business automation</h4>
  <p>Lorem Ipsum has been the industry's standard dummy text ever since the 1500s,</p>
  <a href="#">Read More ▸</a>
</article>
<article class="abs card" style="left:457px">
  <div class="img" style="background:linear-gradient(135deg,#3d4652,#1d2024)" role="img" aria-label="Person working at a desk with a large monitor"></div>
  <div class="meta"><span><svg width="12" height="13"><circle cx="6" cy="4" r="3" fill="none" stroke="#ffcc00" stroke-width="1.3"/><path d="M1 12a5 5 0 0 1 10 0" fill="none" stroke="#ffcc00" stroke-width="1.3"/></svg>By Admin</span><span><svg width="13" height="13"><rect x="1" y="2" width="11" height="10" fill="none" stroke="#ffcc00" stroke-width="1.2"/><path d="M1 5h11" stroke="#ffcc00"/></svg>Jan 18,2022</span></div>
  <h4>Business automation</h4>
  <p>Lorem Ipsum has been the industry's standard dummy text ever since the 1500s,</p>
  <a href="#">Read More ▸</a>
</article>
<article class="abs card" style="left:771px">
  <div class="img" style="background:linear-gradient(135deg,#f3f3f3,#a8a8a8)" role="img" aria-label="Black wireframe cubes on a white surface"></div>
  <div class="meta"><span><svg width="12" height="13"><circle cx="6" cy="4" r="3" fill="none" stroke="#ffcc00" stroke-width="1.3"/><path d="M1 12a5 5 0 0 1 10 0" fill="none" stroke="#ffcc00" stroke-width="1.3"/></svg>By Admin</span><span><svg width="13" height="13"><rect x="1" y="2" width="11" height="10" fill="none" stroke="#ffcc00" stroke-width="1.2"/><path d="M1 5h11" stroke="#ffcc00"/></svg>Jan 18,2022</span></div>
  <h4>Business automation</h4>
  <p>Lorem Ipsum has been the industry's standard dummy text ever since the 1500s,</p>
  <a href="#">Read More ▸</a>
</article>

<!-- footer -->
<div class="abs brand" style="left:58px;top:3590px">plovrek</div>
<div class="abs footer-col" style="left:337px;top:3592px">
  <h5>Site Map</h5>
  <ul><li>- Home</li><li>- About Us</li><li>- Services</li><li>- News</li><li>- Contact Us</li></ul>
</div>
<div class="abs footer-col" style="left:613px;top:3592px">
  <h5>Contact Us</h5>
  <div class="contact-row"><svg width="14" height="18" viewBox="0 0 14 18"><path d="M7 17s6-6.5 6-10.5A6 6 0 0 0 1 6.5C1 10.5 7 17 7 17z" fill="#ffcc00"/><circle cx="7" cy="6.5" r="2.2" fill="#151515"/></svg><span>101 - Lorem ipsum is dummy printing text</span></div>
  <div class="contact-row"><svg width="16" height="16" viewBox="0 0 24 24"><path d="M5 3h4l2 5-2.5 1.5a11 11 0 0 0 6 6L16 13l5 2v4a2 2 0 0 1-2 2A16 16 0 0 1 3 5a2 2 0 0 1 2-2z" fill="#ffcc00"/></svg><span>+46 8 555 0142</span></div>
  <div class="contact-row"><svg width="18" height="13" viewBox="0 0 18 13"><rect width="18" height="13" rx="2" fill="#ffcc00"/><path d="M1 1l8 6 8-6" fill="none" stroke="#151515" stroke-width="1.4"/></svg><span>hello@plovrek.com</span></div>
</div>
<div class="abs footer-col" style="left:888px;top:3592px">
  <h5>Follow Us</h5>
  <div class="social"><span>Vb</span><span>Vl</span><span>Px</span></div>
</div>

<div class="abs bottom-bar"><span>© 2022 plovrek-All Right Reserved,</span><span>Privacy and terms of use</span></div>

</body>
</html>
```